Venue Booking Site

I would like a venue directory and booking website designed. The idea is that end users will come to the site to find venues for weddings, parties, events etc. They will be able to find the venue based on many criteria, the most important ones are availability and location - they will be able to see in real time which venues are available for the desired dates and areas.

Venues will be able to use the website as a reservation management tool, receive payments for bookings through the site and be able to manage bookings on the go. This will be made into an app. It needs to be developed in bootstrap. Brand name to be used: Mirqona. Venue, place and space bookings.

Target audience - end users - anyone who is looking for a venue. For Community members it will provide an easy way to find a suitable venue
Outline what dates and times the venue is available
Outline costs involved in booking the venue
Search via many other criteria
It will allow the customer to book and pay for the venue online in one smooth process

Clients: Venue managers - particularly focussing on not for profit businesses eg, GHAs, community hall managers, small business managers. These people typically use paper based systems yet and do not use websites so it needs to be very user friendly. Future growth to restaurants, pubs, event venues who have a stronger familiarity with computers and who might already use their own booking management tool - so this needs to be able to link in with their system.

What need will this meet for venue managers:
This tool provides venues with greater visibility, promotion and advertising of their venue
This allows more customers to find them and book with them
This tool will be offered to not-for-profit venue managers for free to better connect them to the community
This means greater profit for these community venues
This means more revenue and jobs created in these communities

Sample of the layout / contents attached. This is not a complete site map as yet as it is a work in progress for final pages.

Small Business

5+ page

Sans Serif

eb2027

• This is a psd file only - one template for each different section, home page, search page, detailed page view, admin back end
• does not need to be coded.
• Note, the golden lantern logo jpeg files were files we were toying with using for this project- but I am happy to use the main mirqona logo- I will let you decide.

```html
<!DOCTYPE html>
<html lang="en">
<head>
<meta charset="utf-8">
<title>Mirqona — Venue Booking</title>
<link rel="stylesheet" href="https://fonts.googleapis.com/css2?family=Arimo:wght@400;700&display=swap">
<style>
  :root {
    --maroon: #8a0a24;
    --maroon-btn: #8c0d2b;
    --black: #000000;
    --header-dark: #111111;
    --header-mid: #3a3a3a;
    --white: #ffffff;
    --ink: #111111;
    --field-edge: #555555;
    --field-fill: #fbf6f8;
    --brand-red: #eb2027;
  }
  * { box-sizing: border-box; margin: 0; padding: 0; }
  html, body { width: 1200px; height: 1000px; overflow: hidden; }
  body {
    position: relative;
    background: var(--maroon);
    font-family: "Arimo", Arial, sans-serif;
    color: var(--ink);
  }
  .page {
    position: absolute; left: 82px; top: 30px; width: 1033px; height: 970px;
    background: var(--white); overflow: hidden;
  }
  .abs { position: absolute; }

  /* Header */
  .site-header {
    left: 0; top: 0; width: 1033px; height: 218px;
    background: linear-gradient(120deg, var(--header-dark) 0%, var(--header-dark) 40%, var(--header-mid) 70%, #1e1e1e 100%);
  }
  .header-swoosh { left: 0; top: 0; }
  .brand {
    left: 90px; top: 88px; display: flex; align-items: center; gap: 14px;
    color: var(--white); font-size: 46px; font-weight: 400; letter-spacing: 1px;
  }
  .brand-mark { width: 24px; height: 24px; background: var(--brand-red); }
  .login-text { color: var(--white); font-size: 22px; white-space: nowrap; line-height: 1; }
  .field-light { background: var(--white); border: 1px solid #cfcfcf; }
  .small-check { background: var(--white); width: 18px; height: 17px; }
  .keep-text { color: var(--white); font-size: 17px; }
  .forgot { color: var(--white); font-size: 17px; text-decoration: underline; }
  .btn {
    display: flex; align-items: center; justify-content: center;
    background: var(--maroon-btn); color: var(--white); font-size: 22px;
    border: 2px solid #c9c0a8; box-shadow: 0 0 0 1px #333, 2px 3px 4px rgba(0,0,0,.6);
  }

  /* Hero */
  .hero-photo {
    left: 0; top: 218px; width: 1033px; height: 255px;
    background:
      radial-gradient(ellipse at 30% 75%, #e0a040 0%, rgba(224,160,64,0) 45%),
      linear-gradient(90deg, #6b3a1a 0%, #c8904e 35%, #e8d6b4 65%, #b7603a 100%);
  }

  /* Navigation */
  .main-nav { left: 0; top: 473px; width: 1033px; height: 72px; background: var(--black); }
  .nav-item { color: var(--white); font-size: 29px; white-space: nowrap; }
  .nav-divider { width: 1px; background: #6a1020; }

  /* Search */
  .map-area {
    left: 26px; top: 596px; width: 245px; height: 234px;
    background: linear-gradient(135deg, #e9e4d8 0%, #d6e4ec 55%, #b9d3e6 100%);
  }
  .search-title { left: 467px; top: 570px; font-size: 29px; }
  .label { font-size: 17px; left: 308px; }
  .field {
    background: var(--field-fill);
    border-top: 3px solid var(--field-edge); border-left: 2px solid var(--field-edge);
    border-bottom: 2px solid #999; border-right: 2px solid #999;
  }
  .cal-icon {
    left: 639px; top: 631px; width: 24px; height: 24px; border-radius: 4px;
    background: linear-gradient(#fff, #ddd); border: 1px solid #aaa;
  }
  .adv-check { left: 790px; top: 848px; width: 17px; height: 17px; background: #888; border: 3px solid #ccc; }
  .adv-text { left: 819px; top: 844px; font-size: 23px; }

  /* Footer */
  .footer-arc { left: 0; top: 870px; }
  .copyright { left: 0; width: 1033px; text-align: center; top: 930px; font-size: 17px; color: var(--ink); }
</style>
</head>
<body>
<div class="page">
  <header class="abs site-header">
    <svg class="abs header-swoosh" width="1033" height="218" viewBox="0 0 1033 218" aria-hidden="true">
      <path d="M0 40 C 40 90, 60 170, 70 218 L 40 218 C 30 160, 15 100, 0 70 Z" fill="#2c2c2c"/>
      <path d="M830 0 C 930 60, 980 150, 1000 218 L 1033 218 C 1010 140, 960 50, 870 0 Z" fill="#1a1a1a"/>
    </svg>
    <div class="abs brand"><span class="brand-mark"></span>mirqona</div>

    <div class="abs login-text" style="left:402px;top:16px;">Venue Login :</div>
    <div class="abs login-text" style="left:455px;top:43px;">User Name</div>
    <div class="abs field-light" style="left:587px;top:43px;width:162px;height:21px;"></div>
    <div class="abs login-text" style="left:767px;top:46px;">Password</div>
    <div class="abs field-light" style="left:892px;top:45px;width:131px;height:22px;"></div>
    <div class="abs small-check" style="left:466px;top:83px;"></div>
    <div class="abs keep-text" style="left:499px;top:81px;">Keep me logged in</div>
    <div class="abs forgot" style="left:831px;top:85px;">Forgot your password?</div>
    <div class="abs btn" style="left:575px;top:118px;width:124px;height:37px;">Login</div>
    <div class="abs btn" style="left:764px;top:118px;width:231px;height:37px;">List My Venue</div>
    <div class="abs login-text" style="left:398px;top:178px;">Total raised for charity :</div>
  </header>

  <div class="abs hero-photo" role="img" aria-label="Photo of a bright hotel restaurant with a breakfast buffet, fruit bowls and flowers in front of white-clothed tables"></div>

  <nav class="abs main-nav">
    <span class="abs nav-item" style="left:26px;top:20px;">Home</span>
    <span class="abs nav-divider" style="left:124px;top:0;height:72px;"></span>
    <span class="abs nav-item" style="left:153px;top:23px;">Venues</span>
    <span class="abs nav-divider" style="left:286px;top:0;height:76px;"></span>
    <span class="abs nav-item" style="left:319px;top:23px;">News &amp; Offers</span>
    <span class="abs nav-divider" style="left:539px;top:0;height:70px;"></span>
    <span class="abs nav-item" style="left:581px;top:18px;">Inspirations</span>
    <span class="abs nav-divider" style="left:757px;top:0;height:70px;"></span>
    <span class="abs nav-item" style="left:789px;top:20px;">Contact</span>
    <span class="abs nav-divider" style="left:922px;top:0;height:72px;"></span>
    <span class="abs nav-item" style="left:948px;top:18px;">FAQ</span>
  </nav>

  <section class="venue-search">
    <div class="abs map-area" role="img" aria-label="Street map of the search area with a venue location marker"></div>
    <h2 class="abs search-title" style="font-weight:400;">Find a venue</h2>

    <div class="abs label" style="top:636px;">Date of event</div>
    <div class="abs field" style="left:490px;top:634px;width:125px;height:20px;"></div>
    <div class="abs cal-icon"></div>

    <div class="abs label" style="top:680px;">Location</div>
    <div class="abs field" style="left:490px;top:676px;width:276px;height:23px;"></div>

    <div class="abs label" style="top:727px;">Venue Capacity</div>
    <div class="abs field" style="left:486px;top:727px;width:280px;height:19px;"></div>

    <div class="abs label" style="top:764px;">Venue Use</div>
    <div class="abs field" style="left:486px;top:766px;width:280px;height:20px;"></div>

    <div class="abs label" style="top:799px;">Key Word Search</div>
    <div class="abs field" style="left:486px;top:801px;width:280px;height:21px;"></div>

    <div class="abs btn" style="left:501px;top:839px;width:140px;height:36px;">Search</div>
    <div class="abs adv-check"></div>
    <div class="abs adv-text">Advanced Search</div>
  </section>

  <footer>
    <svg class="abs footer-arc" width="1033" height="100" viewBox="0 0 1033 100" aria-hidden="true">
      <path d="M0 93 Q 516 -30 1033 78 L 1033 100 L 0 100 Z" fill="var(--maroon)"/>
    </svg>
    <p class="abs copyright">Copyright 2014 mirqona</p>
  </footer>
</div>
</body>
</html>
```